Business Card Design Project

Hi

I have a draft of a business card which I need smarting up. I have attached the pdf of this.
The information on the front is correct.
The information on the back should contain:
Project Management, Consulting, Master Systems Integrator, Datacenter, Relocations, Restacks. I want this spiraling around the back

Can you change the telephone number to +65 8476 2153.

Target Market(s)

Chief Technology Officers of large multi-nationals

Industry/Entity Type

Business

Requirements
Must have
• My logo - Vorbelt (attached)
The orange and blue colour running around the edge

```html
<!DOCTYPE html>
<html lang="en">
<head>
<meta charset="utf-8">
<title>Vorbelt Business Card</title>
<link rel="stylesheet" href="https://fonts.googleapis.com/css2?family=Arimo:wght@400;700&display=swap">
<style>
  :root {
    --backdrop: #3b3b3d;
    --card: #ffffff;
    --edge-orange: #f39a2b;
    --edge-blue: #6fcfe0;
    --ink: #4b4441;
    --accent-orange: #f08a1c;
    --accent-blue: #3bbfd6;
    --symbol-grey: #4a4542;
    --disc-orange: #f59b2e;
    --disc-blue: #7fd0df;
  }
  * { box-sizing: border-box; margin: 0; padding: 0; }
  html, body {
    width: 1200px;
    height: 700px;
    overflow: hidden;
    background: var(--backdrop);
    font-family: "Arimo", Arial, sans-serif;
  }
  .canvas {
    position: relative;
    width: 1200px;
    height: 700px;
  }
  .card {
    position: absolute;
    top: 200px;
    width: 525px;
    height: 300px;
    background: var(--card);
    border: 3px solid var(--edge-orange);
    box-shadow: inset 0 0 0 3px var(--card), inset 0 0 0 5px var(--edge-blue);
    overflow: hidden;
  }
  .card--back { left: 50px; }
  .card--front { left: 625px; }

  /* Back */
  .service-list {
    position: absolute;
    top: 34px;
    left: 36px;
    list-style: none;
    color: var(--accent-orange);
    font-size: 11px;
    line-height: 17px;
  }
  .service-list li::before { content: "- "; }
  .service-list li:nth-child(1) { padding-left: 40px; }
  .service-list li:nth-child(2) { padding-left: 32px; }
  .service-list li:nth-child(3) { padding-left: 24px; }
  .service-list li:nth-child(4) { padding-left: 16px; }
  .service-list li:nth-child(5) { padding-left: 8px; }
  .brand-disc {
    position: absolute;
    right: 14px;
    bottom: 22px;
    width: 250px;
    height: 250px;
  }

  /* Front */
  .brand {
    position: absolute;
    top: 30px;
    left: 30px;
    display: flex;
    align-items: flex-end;
    gap: 14px;
  }
  .brand-square {
    width: 68px;
    height: 68px;
    background: var(--symbol-grey);
  }
  .brand-name {
    font-size: 50px;
    font-weight: 400;
    color: var(--ink);
    line-height: 1;
    letter-spacing: -0.5px;
  }
  .contact {
    position: absolute;
    top: 120px;
    left: 34px;
    color: var(--ink);
    font-size: 11px;
    line-height: 15px;
  }
  .contact-name { font-size: 15px; font-weight: 700; line-height: 18px; }
  .contact-role { font-size: 11px; font-weight: 700; margin-bottom: 12px; }
  .contact-label { color: var(--accent-blue); font-weight: 700; }
  .contact-address { margin-top: 2px; }
</style>
</head>
<body>
<main class="canvas">

  <section class="card card--back" aria-label="Card back">
    <ul class="service-list">
      <li>Project Management</li>
      <li>Consulting</li>
      <li>Master Systems Integrator</li>
      <li>Datacenter</li>
      <li>Relocations</li>
      <li>Restacks</li>
    </ul>
    <svg class="brand-disc" viewBox="0 0 250 250" role="img" aria-label="Large brand symbol area in orange, blue and charcoal">
      <defs>
        <linearGradient id="disc-tones" x1="0" y1="0" x2="1" y2="1">
          <stop offset="0" stop-color="var(--disc-orange)"/>
          <stop offset="0.5" stop-color="var(--disc-blue)"/>
          <stop offset="1" stop-color="var(--symbol-grey)"/>
        </linearGradient>
      </defs>
      <circle cx="125" cy="125" r="125" fill="url(#disc-tones)"/>
    </svg>
  </section>

  <section class="card card--front" aria-label="Card front">
    <div class="brand">
      <span class="brand-square" aria-hidden="true"></span>
      <span class="brand-name">Vorbelt</span>
    </div>
    <div class="contact">
      <p class="contact-name">Marcus Hale</p>
      <p class="contact-role">Director</p>
      <p>Vorbelt Pte Ltd</p>
      <p><span class="contact-label">T:</span> +65 8476 2153</p>
      <p><span class="contact-label">E:</span> marcus.hale@vorbelt.com</p>
      <p><span class="contact-label">W:</span> www.vorbelt.com</p>
      <p class="contact-address">21 Keppel Quay, #05-12 Harbour Point, Singapore 098731</p>
    </div>
  </section>

</main>
</body>
</html>
```